Business Card Design

we specialise in supply of custom uniforms - teamwear to Schools and sporting clubs, see our website: www.kestrelkitworks.com.au, our main corporate colour is black and white, with small amount of gold/yellow

Industry/Entity Type

Business

Contact Information for Business Card

Kestrel Kit Works
Rowan Petrakis
Ph 03 6219 8805
Mobile 0418 262 740
email: rowan@kestrelkitworks.com.au
www.kestrelkitworks.com.au
like us on facebook

Requirements
Must have
• modern look & feel

```html
<!DOCTYPE html>
<html lang="en">
<head>
<meta charset="utf-8">
<title>Kestrel Kit Works – Business Card</title>
<link href="https://fonts.googleapis.com/css2?family=Arimo:wght@400;700&family=Tinos&display=swap" rel="stylesheet">
<style>
  :root {
    --backdrop: #d9d9d9;
    --card-white: #ffffff;
    --card-dark: #262425;
    --accent-gold: #f1d21e;
    --ink-black: #111111;
    --text-light: #f4f4f4;
  }
  * { margin: 0; padding: 0; box-sizing: border-box; }
  html, body {
    width: 1200px; height: 743px; overflow: hidden;
    background: var(--backdrop);
  }
  .business-card {
    position: absolute; left: 100px; top: 84px;
    width: 1000px; height: 575px;
    background: var(--card-dark);
    overflow: hidden;
  }
  .card-top {
    position: absolute; left: 0; top: 0;
    width: 100%; height: 300px;
    background: var(--card-white);
    border-bottom: 6px solid var(--accent-gold);
  }
  .brand-mark {
    position: absolute; left: 56px; top: 92px;
    display: flex; align-items: center; gap: 18px;
  }
  .brand-dot {
    width: 46px; height: 46px; border-radius: 50%;
    background: var(--accent-gold);
  }
  .brand-name {
    font-family: "Arimo", Arial, sans-serif;
    font-weight: 700; font-size: 48px;
    color: var(--ink-black); letter-spacing: -0.5px;
  }
  .identity {
    position: absolute; left: 38px; top: 360px;
    font-family: "Tinos", "Times New Roman", serif;
    color: var(--accent-gold);
  }
  .company-name { font-size: 40px; line-height: 1; }
  .person-name { font-size: 38px; line-height: 1; margin: 48px 0 0 30px; }
  .contact-list {
    position: absolute; left: 600px; top: 330px;
    list-style: none;
    font-family: "Arimo", Arial, sans-serif;
    color: var(--text-light);
  }
  .contact-item {
    display: flex; align-items: center; gap: 18px;
    height: 56px; font-size: 22px;
  }
  .contact-icon { width: 26px; height: 26px; flex: none; }
  .contact-icon path, .contact-icon rect, .contact-icon circle { fill: var(--accent-gold); }
  .contact-icon .stroke { fill: none; stroke: var(--card-dark); stroke-width: 1.6; }
</style>
</head>
<body>
  <section class="business-card">
    <div class="card-top">
      <div class="brand-mark">
        <span class="brand-dot"></span>
        <span class="brand-name">Kestrel Kit Works</span>
      </div>
    </div>

    <div class="identity">
      <p class="company-name">Kestrel Kit Works</p>
      <p class="person-name">Rowan Petrakis</p>
    </div>

    <ul class="contact-list">
      <li class="contact-item">
        <svg class="contact-icon" viewBox="0 0 24 24" aria-hidden="true">
          <path d="M6.6 10.8c1.4 2.8 3.8 5.1 6.6 6.6l2.2-2.2c.3-.3.7-.4 1-.2 1.1.4 2.3.6 3.6.6.6 0 1 .4 1 1V20c0 .6-.4 1-1 1C10.6 21 3 13.4 3 4c0-.6.4-1 1-1h3.5c.6 0 1 .4 1 1 0 1.3.2 2.5.6 3.6.1.3 0 .7-.2 1l-2.3 2.2z"/>
        </svg>
        <span>03 6219 8805</span>
      </li>
      <li class="contact-item">
        <svg class="contact-icon" viewBox="0 0 24 24" aria-hidden="true">
          <rect x="6" y="1.5" width="12" height="21" rx="2"/>
          <rect class="stroke" x="8" y="4" width="8" height="14"/>
        </svg>
        <span>0418 262 740</span>
      </li>
      <li class="contact-item">
        <svg class="contact-icon" viewBox="0 0 24 24" aria-hidden="true">
          <rect x="1.5" y="5" width="21" height="14" rx="1"/>
          <path class="stroke" d="M2.5 6l9.5 7.5L21.5 6M2.5 18l7-6.5M21.5 18l-7-6.5"/>
        </svg>
        <span>rowan@kestrelkitworks.com.au</span>
      </li>
      <li class="contact-item">
        <svg class="contact-icon" viewBox="0 0 24 24" aria-hidden="true">
          <circle cx="12" cy="12" r="10.5"/>
          <path class="stroke" d="M1.5 12h21M12 1.5v21M12 1.5c-5 5-5 16 0 21M12 1.5c5 5 5 16 0 21M3.5 6.5h17M3.5 17.5h17"/>
        </svg>
        <span>www.kestrelkitworks.com.au</span>
      </li>
    </ul>
  </section>
</body>
</html>
```